Nordisk Boligkontor

Company is in: Denmark - Copenhagen
It sells: Restaurants and café buildings
Companys age: 25 years
Main benefit: trust with over 25 years experience

```html
<!DOCTYPE html>
<html lang="da">
<head>
<meta charset="utf-8">
<title>Nordisk Boligkontor</title>
<link href="https://fonts.googleapis.com/css2?family=Ubuntu:wght@400;500;700&display=swap" rel="stylesheet">
<style>
:root{
  --sky:#1ca3dc;
  --sky-deep:#0e86c2;
  --accent:#16a6e0;
  --ink:#333333;
  --ink-soft:#555555;
  --paper:#ffffff;
  --mist:#e2e2e2;
  --night:#3b3b3d;
  --night-deep:#0e0e0f;
  --foot-text:#e6e6e6;
  --foot-muted:#9a9a9a;
}
*{margin:0;padding:0;box-sizing:border-box}
html,body{width:1100px;height:1200px;overflow:hidden}
body{font-family:'Ubuntu',sans-serif;position:relative;
  background:linear-gradient(180deg,var(--sky) 0,#1597d2 462px,var(--mist) 462px,#f5f5f5 803px,var(--night) 803px,var(--night-deep) 1200px);}
.abs{position:absolute}

.util-links{left:906px;top:10px;font-size:12px;color:#e8f6ff;letter-spacing:.5px}
.util-links span{margin:0 14px}
.brand{left:76px;top:44px;font-size:31px;font-weight:700;color:var(--paper);letter-spacing:1px;text-transform:uppercase}
.search{left:764px;top:64px;width:238px;height:30px;border-radius:15px;background:var(--paper);font-size:11px;color:#888;padding:7px 10px}
.search-btn{left:976px;top:61px;width:34px;height:34px;border-radius:50%;background:radial-gradient(circle at 40% 35%,#7fd3ff,#0a6fae);border:2px solid #dff3ff}

.nav{left:69px;top:122px;width:954px;height:45px;border-radius:14px;background:linear-gradient(#ffffff,#d9d9d9);box-shadow:0 2px 3px rgba(0,0,0,.2)}
.nav-item{top:122px;height:45px;line-height:45px;font-size:13px;font-weight:500;color:#333;transform:translateX(-50%);white-space:nowrap}
.nav-sep{top:126px;width:1px;height:37px;background:#c4c4c4}
.nav-active{left:210px;top:109px;width:116px;height:58px;background:linear-gradient(#3a3a3a,#0c0c0c)}
.nav-fold{left:326px;top:109px;width:0;height:0;border-left:12px solid #111;border-top:12px solid transparent}

.hero{left:69px;top:178px;width:964px;height:360px;border-radius:16px;background:var(--paper);box-shadow:0 3px 6px rgba(0,0,0,.25)}
.hero-photo{left:82px;top:191px;width:631px;height:334px;border-radius:10px;background:linear-gradient(135deg,#b5895a 0%,#d7b98c 35%,#9bb8d4 60%,#6a4a30 100%)}
.hero-band{left:82px;top:191px;width:631px;height:88px;border-radius:10px 10px 0 0;background:rgba(40,40,40,.6)}
.hero-title{left:102px;top:196px;font-size:28px;font-weight:700;color:var(--accent);letter-spacing:1.5px}
.hero-sub{left:102px;top:224px;font-size:23px;color:var(--paper);line-height:24px;letter-spacing:.5px}
.find{left:721px;top:191px;width:299px;height:334px;background:var(--sky-deep);border-radius:0 10px 10px 0}
.find-pill{left:739px;top:198px;width:272px;height:40px;border-radius:14px;background:linear-gradient(#fff,#d8d8d8)}
.find-label{left:819px;top:203px;font-size:25px;font-weight:700;color:#222}
.map{left:736px;top:246px;width:268px;height:267px;border-radius:10px;background:linear-gradient(135deg,#d4d4d4,#bdbdbd)}

.card{top:568px;width:276px;height:325px;border-radius:18px;background:linear-gradient(#ffffff,#ececec);box-shadow:0 2px 6px rgba(0,0,0,.25)}
.card-img{top:583px;width:244px;height:205px;border-radius:12px}
.card-title{top:801px;font-size:22px;font-weight:500;color:var(--ink);letter-spacing:.5px}
.card-text{top:830px;font-size:12.5px;line-height:18px;color:var(--ink-soft);width:230px}
.card-more{top:870px;font-size:12.5px;color:#333}

.foot-h{font-size:24px;color:var(--paper)}
.foot-p{font-size:12px;line-height:18px;color:var(--foot-text)}
.divider{left:500px;top:920px;height:240px;border-left:1px dashed #777}
.social{top:1157px;width:34px;height:34px;border-radius:9px;background:linear-gradient(#f2f2f2,#9a9a9a)}
.contact-row{font-size:12px;color:var(--foot-text);line-height:18px}
.contact-row b{display:inline-block;font-weight:400;width:48px}
.legal{left:91px;top:1144px;font-size:12.5px;line-height:18px;color:var(--foot-muted)}
.foot-brand{left:819px;top:1146px;font-size:18px;font-weight:700;color:#555;letter-spacing:1px;text-transform:uppercase}
</style>
</head>
<body>

<div class="abs util-links">Sitemap<span>/</span>Prient</div>
<div class="abs brand">Nordisk Boligkontor</div>
<div class="abs search">-----Search Property----------</div>
<div class="abs search-btn"></div>

<nav>
  <div class="abs nav"></div>
  <div class="abs nav-active"></div>
  <div class="abs nav-fold"></div>
  <div class="abs nav-sep" style="left:193px"></div>
  <div class="abs nav-sep" style="left:347px"></div>
  <div class="abs nav-sep" style="left:510px"></div>
  <div class="abs nav-sep" style="left:711px"></div>
  <div class="abs nav-sep" style="left:878px"></div>
  <div class="abs nav-item" style="left:135px">HOME</div>
  <div class="abs nav-item" style="left:266px;color:#fff">COMPANY INFO</div>
  <div class="abs nav-item" style="left:422px">SALES LIST</div>
  <div class="abs nav-item" style="left:608px">LINKS / DOWNLOAD</div>
  <div class="abs nav-item" style="left:793px">NEWSLETTER</div>
  <div class="abs nav-item" style="left:937px">CONTACT</div>
</nav>

<section>
  <div class="abs hero"></div>
  <div class="abs hero-photo" role="img" aria-label="Two builders in hard hats reviewing plans under a timber roof frame"></div>
  <div class="abs hero-band"></div>
  <div class="abs hero-title">NORDISK BOLIGKONTOR</div>
  <div class="abs hero-sub" style="top:226px">has over 25 years experience<br>in the industry,</div>
  <div class="abs find"></div>
  <div class="abs find-pill"></div>
  <svg class="abs" style="left:764px;top:196px" width="44" height="42" viewBox="0 0 44 42">
    <circle cx="26" cy="16" r="11" fill="#dbe9f7" stroke="#5a6b80" stroke-width="3"/>
    <line x1="18" y1="24" x2="5" y2="37" stroke="#3b4a5c" stroke-width="5" stroke-linecap="round"/>
  </svg>
  <div class="abs find-label">Find us</div>
  <div class="abs map" role="img" aria-label="Street map showing the office location"></div>
</section>

<section>
  <div class="abs card" style="left:91px"></div>
  <div class="abs card-img" style="left:107px;background:linear-gradient(#6f97c8,#b7c4cf 60%,#8d8f8a)" role="img" aria-label="Modern office building with a round glass tower"></div>
  <div class="abs card-title" style="left:108px">BUSINESS WEEK</div>
  <div class="abs card-text" style="left:108px">Se Hvilke Atraktive Forretninger Vi Anbefaler I Denne Uge</div>
  <div class="abs card-more" style="left:272px">Readmore...</div>

  <div class="abs card" style="left:412px"></div>
  <div class="abs card-img" style="left:428px;background:linear-gradient(160deg,#3f5a9c,#9aa7c8 55%,#c9d0de)" role="img" aria-label="Angular glass skyscraper forming an arch"></div>
  <div class="abs card-title" style="left:428px">SOG STORES</div>
  <div class="abs card-text" style="left:430px">Se Hvilke Atraktive Forretninger Vi Anbefaler I Denne Uge</div>
  <div class="abs card-more" style="left:600px">Readmore...</div>

  <div class="abs card" style="left:735px"></div>
  <div class="abs card-img" style="left:749px;background:linear-gradient(#7fb2e6,#c8b8a2 60%,#6c6a66)" role="img" aria-label="Tall stone tower with a green copper roof among high-rises"></div>
  <div class="abs card-title" style="left:753px">CONTACT US</div>
  <div class="abs card-text" style="left:755px">Se Hvilke Atraktive Forretninger Vi Anbefaler I Denne Uge</div>
  <div class="abs card-more" style="left:921px">Readmore...</div>
</section>

<footer>
  <svg class="abs" style="left:90px;top:910px" width="46" height="70" viewBox="0 0 46 70">
    <rect x="4" y="10" width="18" height="58" fill="#8fc8ea" stroke="#dff" stroke-width="1"/>
    <rect x="22" y="2" width="20" height="62" fill="#5aa6d6" stroke="#dff" stroke-width="1"/>
  </svg>
  <div class="abs foot-h" style="left:148px;top:929px">About <b>NBK's</b> website.</div>
  <p class="abs foot-p" style="left:98px;top:999px;width:394px">Nordisk Boligkontor has over 25 years experience in the industry, it has given us a thorough knowledge of the industry's many subtleties and we can therefore say with certainty that you will be in good hands with Nordisk Boligkontor, whether you want to sell or buy a restaurant business.</p>

  <div class="abs divider"></div>

  <svg class="abs" style="left:511px;top:914px" width="50" height="48" viewBox="0 0 50 48">
    <ellipse cx="25" cy="42" rx="22" ry="5" fill="#999"/>
    <rect x="12" y="4" width="24" height="38" fill="#7d96ac" stroke="#e8eef3"/>
  </svg>
  <div class="abs foot-h" style="left:570px;top:925px">Testimonial</div>
  <p class="abs foot-p" style="left:521px;top:967px;width:215px;text-align:justify">Nordisk Boligkontor has over 25 years experience in the industry, it has given us a thorough knowledge of the industry's many subtleties and we can therefore say with certainty that you will be in good hands with Nordisk Boligkontor,</p>

  <svg class="abs" style="left:518px;top:1104px" width="46" height="50" viewBox="0 0 46 50">
    <ellipse cx="20" cy="44" rx="18" ry="5" fill="#666"/>
    <path d="M6 26 L17 40 L40 4" fill="none" stroke="#38b43a" stroke-width="6" stroke-linecap="round" stroke-linejoin="round"/>
  </svg>
  <div class="abs foot-h" style="left:571px;top:1117px">Join us <b>on</b></div>
  <div class="abs social" style="left:565px"></div>
  <div class="abs social" style="left:610px;border-radius:50%"></div>
  <div class="abs social" style="left:656px"></div>
  <div class="abs social" style="left:701px"></div>
  <div class="abs social" style="left:748px"></div>

  <svg class="abs" style="left:805px;top:918px" width="48" height="40" viewBox="0 0 48 40">
    <rect x="2" y="6" width="42" height="28" rx="3" fill="#eef3f8" stroke="#9bb" transform="rotate(-8 24 20)"/>
    <rect x="8" y="12" width="10" height="12" fill="#7aa6cc" transform="rotate(-8 24 20)"/>
  </svg>
  <div class="abs foot-h" style="left:858px;top:918px">Contact us</div>
  <div class="abs" style="left:817px;top:974px;font-size:13.5px;color:var(--foot-text)">NORDISK BOLIGKONTOR</div>
  <div class="abs" style="left:818px;top:999px;font-size:12px;color:var(--accent)">Contact Information:</div>
  <div class="abs contact-row" style="left:818px;top:1017px">
    <div><b>Phone</b>&nbsp;:&nbsp;&nbsp;&nbsp;+45 40 12 34 56</div>
    <div><b>Fax</b>&nbsp;:&nbsp;&nbsp;&nbsp;+45 40 12 34 57</div>
    <div><b>Address</b>&nbsp;:&nbsp;&nbsp;Søtorvet 14, 1371 København</div>
    <div><b>E-mail:</b>&nbsp;&nbsp;:&nbsp;&nbsp;kontakt@nordiskbolig.dk</div>
  </div>

  <div class="abs legal">Copyright © 2011 FJORDHUS HOLDING APS All rights reserved.<br>Disclaimer &nbsp;|&nbsp; Sitemap &nbsp;|&nbsp; Privacy Policy</div>
  <div class="abs foot-brand">Nordisk Boligkontor</div>
</footer>

</body>
</html>
```